Design KWN's Corporate Christmas Card

This project is to design a highly attractive and professional looking corporate Christmas card. The card is A5 size (folded into two halves of A6 either portrait or landscape) plus an A6 matching envelope. The card will be printed in-house onto white matt or pearlised white or cream card stock with matching envelope. The printing will be through a 1200x1200 good-quality colour laser printer. Just to clarify, the cards are A5 size folded into two. The envelopes are A6 size (or slightly larger) to accommodate the card.

The inside of the card will be individually personalised as follows:

KWN wishes
> of

Merry Christmas
and a
Happy New Year

The text in > will be personalised through the mail merge process to our database.

The outside of the card must have either a picture or a graphic or combination that is attractive and professional.

The major criteria for this project are:

* ability to look professional even when printed on normal card stock and office laser printer
* attractiveness
* professionalism
* good corporate identity

Our company logo is attached. Attached are also samples of 6x cards we have seen that are good (YES) and 1x that is bad (NO). Bad in the sense that because we are using normal card stock and office laser printer (albeit good quality printer) the colour will not come out looking good. Please do not incorporate any metallic gilting because the printer will not be able to do that. Also please do not design to the very edge of the paper because the printer won't print to the edge.

Many thanks and best of luck.

```html
<!DOCTYPE html>
<html lang="en">
<head>
<meta charset="utf-8">
<title>KWN Corporate Christmas Card</title>
<link rel="stylesheet" href="https://fonts.googleapis.com/css2?family=Inter:wght@300;400;500&family=Cormorant+Garamond:ital,wght@1,400;1,500&display=swap">
<style>
  :root {
    --page: #ffffff;
    --card: #ffffff;
    --ink: #1a1a1a;
    --muted: #555555;
    --label: #444444;
    --brand: #2296d3;
    --ice: #cfe9f1;
    --frost: #a9dbe7;
    --teal: #6cc4d6;
    --rule: #b9dde8;
    --shadow: rgba(0, 0, 0, 0.45);
  }
  * { box-sizing: border-box; margin: 0; padding: 0; }
  html, body { width: 1200px; height: 605px; overflow: hidden; background: var(--page); }
  .sheet { position: relative; width: 1200px; height: 605px; font-family: "Inter", Arial, sans-serif; color: var(--ink); }

  .panel {
    position: absolute;
    background: var(--card);
    border: 1px solid #d6d6d6;
    box-shadow: 5px 6px 7px var(--shadow);
  }
  .panel--front { left: 64px; top: 84px; width: 297px; height: 420px; }
  .panel--inside { left: 388px; top: 84px; width: 296px; height: 420px; }
  .panel--envelope { left: 708px; top: 183px; width: 456px; height: 321px; }

  .presentation-title {
    position: absolute; left: 708px; top: 84px;
    font-weight: 300; font-size: 20px; color: var(--ink); letter-spacing: 0.2px;
  }
  .panel-label {
    position: absolute; top: 530px;
    font-weight: 300; font-size: 14px; letter-spacing: 3px; color: var(--label);
    text-align: center;
  }
  .panel-label--front { left: 64px; width: 297px; }
  .panel-label--inside { left: 388px; width: 296px; }
  .panel-label--envelope { left: 708px; width: 456px; }

  /* brand mark stand-in */
  .brand-name {
    position: absolute;
    display: flex; align-items: center; gap: 5px;
    font-family: "Inter", Arial, sans-serif; font-weight: 500;
    color: var(--brand); letter-spacing: 6px;
  }
  .brand-name__square { width: 10px; height: 10px; background: var(--brand); }

  /* front */
  .front-greeting {
    position: absolute; left: 0; top: 26px; width: 100%;
    text-align: center; font-weight: 300; font-size: 9.5px; line-height: 12px; color: var(--muted);
  }
  .front-tree {
    position: absolute; left: 37px; top: 79px; width: 222px; height: 244px;
    background: linear-gradient(180deg, #eef7fa 0%, var(--ice) 30%, var(--frost) 65%, var(--teal) 100%);
    clip-path: polygon(50% 0, 100% 100%, 0 100%);
  }
  .panel--front .brand-name { left: 108px; top: 343px; font-size: 22px; }

  /* inside */
  .inside-snow {
    position: absolute; left: 52px; top: 12px; width: 192px; height: 396px;
    background: radial-gradient(ellipse at center, rgba(169, 219, 231, 0.35) 0%, rgba(169, 219, 231, 0.12) 60%, rgba(255, 255, 255, 0) 100%);
  }
  .panel--inside .brand-name { left: 111px; top: 56px; font-size: 20px; }
  .inside-message {
    position: absolute; left: 0; width: 100%; text-align: center;
    font-family: "Cormorant Garamond", Georgia, serif; font-style: italic; color: var(--ink);
  }
  .inside-message--wishes { top: 105px; font-size: 17px; }
  .inside-message--of { top: 154px; font-size: 17px; }
  .inside-message--merry { top: 205px; font-size: 25px; letter-spacing: 0.5px; }
  .inside-message--and { top: 243px; font-size: 15px; }
  .inside-message--happy { top: 272px; font-size: 25px; letter-spacing: 0.5px; }
  .inside-rule { position: absolute; left: 52px; width: 187px; height: 1px; background: var(--rule); }
  .inside-rule--upper { top: 148px; }
  .inside-rule--lower { top: 196px; }

  /* envelope */
  .panel--envelope .brand-name { left: 26px; top: 36px; font-size: 17px; letter-spacing: 4px; }
  .envelope-band {
    position: absolute; left: 32px; top: 64px; width: 57px; height: 220px;
    background: linear-gradient(180deg, var(--frost) 0%, #d4edf4 55%, rgba(255, 255, 255, 1) 100%);
  }
</style>
</head>
<body>
<main class="sheet">
  <p class="presentation-title">A5 size X'mas Card folded in to A6</p>

  <section class="panel panel--front" aria-label="Card front">
    <p class="front-greeting">wishing you and your loved ones<br>a very joyous holiday<br>and a<br>wonderful and prosperous new year.</p>
    <div class="front-tree" role="img" aria-label="Layered pale blue Christmas tree with white snow dots"></div>
    <div class="brand-name"><span class="brand-name__square"></span>KWN</div>
  </section>

  <section class="panel panel--inside" aria-label="Card inside">
    <div class="inside-snow" role="img" aria-label="Scattered pale blue snow dots"></div>
    <div class="brand-name"><span class="brand-name__square"></span>KWN</div>
    <p class="inside-message inside-message--wishes">wishes</p>
    <span class="inside-rule inside-rule--upper"></span>
    <p class="inside-message inside-message--of">of</p>
    <span class="inside-rule inside-rule--lower"></span>
    <p class="inside-message inside-message--merry">Merry Christmas</p>
    <p class="inside-message inside-message--and">and a</p>
    <p class="inside-message inside-message--happy">Happy New Year</p>
  </section>

  <section class="panel panel--envelope" aria-label="Envelope">
    <div class="brand-name"><span class="brand-name__square"></span>KWN</div>
    <div class="envelope-band" role="img" aria-label="Vertical blue band with falling snow dots fading to white"></div>
  </section>

  <p class="panel-label panel-label--front">FRONT</p>
  <p class="panel-label panel-label--inside">INSIDE</p>
  <p class="panel-label panel-label--envelope">ENVELOPE</p>
</main>
</body>
</html>
```